Business cards for a new business: Willow Brook Calm Healing

I would like for the card to include a lotus. The business is a healing practice so I'd like the overall colours to be pink and green and for it to have a soft feel. The name of the practice is
"Willow Brook Calm Healing", which I'd like to be included, as well as the words: "Energetic and spiritual healing to restore health, harmony and wellbeing". Also, my name - Tarik and the number: 5391 6048

Target Market(s)

Everyone interested in personal healing!

Industry/Entity Type

Business

Contact Information for Business Card

As above……..could be single or double-sided
I'd like the font for the name of the practice and my name to be in green and be a flowing, but simple font - elegant.
The background to be a light pink. See below for colours

Colors
f9d9e8
eea4c8
e567a6
d0ebe7
86cfc6
33b7a4

Requirements
Must have
• See above
Nice to have
• See above

```html
<!DOCTYPE html>
<html lang="en">
<head>
<meta charset="utf-8">
<title>Willow Brook Calm Healing – Business Cards</title>
<link rel="stylesheet" href="https://fonts.googleapis.com/css2?family=Pinyon+Script&family=Playball&family=Pathway+Gothic+One&display=swap">
<style>
  :root {
    --paper: #ffffff;
    --pink-light: #f9d9e8;
    --pink-mid: #eea4c8;
    --pink-strong: #e567a6;
    --pink-deep: #de3f95;
    --green-light: #d0ebe7;
    --green-mid: #86cfc6;
    --green-strong: #1fae9a;
    --crop: #333333;
  }
  * { margin: 0; padding: 0; box-sizing: border-box; }
  html, body { width: 1200px; height: 867px; overflow: hidden; background: var(--paper); }
  .sheet { position: relative; width: 1200px; height: 867px; }

  .crop-marks { position: absolute; inset: 0; }

  .card {
    position: absolute;
    top: 148px;
    width: 335px;
    height: 554px;
    overflow: hidden;
    background:
      radial-gradient(ellipse 60% 40% at 30% 20%, rgba(255,255,255,.55), transparent 70%),
      radial-gradient(ellipse 50% 35% at 75% 60%, rgba(255,255,255,.5), transparent 70%),
      radial-gradient(ellipse 55% 30% at 25% 85%, rgba(255,255,255,.45), transparent 70%),
      radial-gradient(ellipse 40% 30% at 85% 15%, rgba(238,164,200,.35), transparent 70%),
      var(--pink-light);
    box-shadow: 6px 10px 14px rgba(0,0,0,.28);
  }
  .card--front { left: 150px; }
  .card--back { left: 653px; }

  .practice-name,
  .practice-subname {
    position: absolute;
    left: 0; right: 0;
    text-align: center;
    font-family: "Pinyon Script", cursive;
    color: var(--green-strong);
    white-space: nowrap;
  }
  .practice-name { top: 34px; font-size: 46px; transform: rotate(-4deg); }
  .practice-subname { top: 330px; font-size: 44px; }

  .lotus-artwork {
    position: absolute;
    left: 32px; top: 80px;
    width: 282px; height: 245px;
    border-radius: 50% 50% 46% 46%;
    background:
      radial-gradient(circle at 50% 30%, #f6c25a 0 9%, transparent 10%),
      radial-gradient(ellipse 45% 45% at 50% 40%, var(--pink-mid), transparent 75%),
      radial-gradient(ellipse 55% 40% at 50% 70%, rgba(255,255,255,.9), transparent 75%);
    opacity: .95;
  }

  .tagline {
    position: absolute;
    left: 0; right: 0; top: 400px;
    text-align: center;
    font-family: "Pathway Gothic One", sans-serif;
    font-size: 29px;
    line-height: 47px;
    color: var(--pink-strong);
  }

  .card--back .practice-name,
  .card--back .practice-subname { color: var(--green-mid); opacity: .85; }
  .card--back .practice-subname { top: 282px; }
  .card--back .lotus-artwork { opacity: .7; }

  .connect-label {
    position: absolute;
    left: 0; right: 0; top: 388px;
    text-align: center;
    font-family: "Playball", cursive;
    font-size: 32px;
    color: var(--pink-deep);
  }
  .contact-line {
    position: absolute;
    left: 0; right: 0; top: 444px;
    text-align: center;
    font-family: "Pathway Gothic One", sans-serif;
    font-size: 50px;
    color: var(--pink-deep);
    word-spacing: 6px;
  }
  .contact-name { margin-right: 14px; }
</style>
</head>
<body>
<div class="sheet">
  <svg class="crop-marks" width="1200" height="867" aria-hidden="true">
    <g stroke="var(--crop)" stroke-width="1">
      <line x1="151" y1="30" x2="151" y2="108"/>
      <line x1="485" y1="30" x2="485" y2="108"/>
      <line x1="653" y1="30" x2="653" y2="108"/>
      <line x1="987" y1="30" x2="987" y2="108"/>
      <line x1="151" y1="742" x2="151" y2="820"/>
      <line x1="485" y1="742" x2="485" y2="820"/>
      <line x1="653" y1="742" x2="653" y2="820"/>
      <line x1="987" y1="742" x2="987" y2="820"/>
      <line x1="33" y1="148" x2="112" y2="148"/>
      <line x1="523" y1="148" x2="613" y2="148"/>
      <line x1="1025" y1="148" x2="1104" y2="148"/>
      <line x1="33" y1="702" x2="112" y2="702"/>
      <line x1="523" y1="702" x2="613" y2="702"/>
      <line x1="1025" y1="702" x2="1104" y2="702"/>
    </g>
  </svg>

  <section class="card card--front">
    <div class="lotus-artwork" role="img" aria-label="Pink water lily with a golden centre"></div>
    <h1 class="practice-name">Willow Brook</h1>
    <h2 class="practice-subname">Calm Healing</h2>
    <p class="tagline">Energetic and spiritual healing<br>to restore health, harmony<br>and wellbeing</p>
  </section>

  <section class="card card--back">
    <div class="lotus-artwork" role="img" aria-label="Soft faded pink water lily"></div>
    <p class="practice-name">Willow Brook</p>
    <p class="practice-subname">Calm Healing</p>
    <p class="connect-label">Connect with:</p>
    <p class="contact-line"><span class="contact-name">Tarik</span> 02 5391 6048</p>
  </section>
</div>
</body>
</html>
```